Maple Hollow - New monument signage for our apartment community

We have a monument sign that we would like to replace with a fresh, clean, and easy to read new design. I've included a couple pictures of the physical sign - people will be seeing this while driving very fast. It needs to be simple and easy to quickly see while driving.

* Maple Hollow
* Newly Renovated!
* www.maplehollowliving-example.com
* 555 - 318 - 7096

Suggestions:
* Bright colors
* Bold fonts
* Focus on phone number being easy to read

*** I attached a picture of something similar we did at one of our other apartment communities (Willowmere townhomes)

Logo Text

Maple Hollow Apartment Community

```html
<!DOCTYPE html>
<html lang="en">
<head>
<meta charset="utf-8">
<title>Maple Hollow – Monument Sign</title>
<link href="https://fonts.googleapis.com/css2?family=Playfair+Display:wght@600;700&family=Josefin+Sans:wght@500;600&display=swap" rel="stylesheet">
<style>
  :root {
    --sign-sky: #0a74bb;
    --sign-navy: #283c92;
    --sign-gold: #f8c24b;
    --sign-white: #ffffff;
    --page: #ffffff;
    --photo-fill: #b9c6d8;
  }
  html, body {
    margin: 0;
    padding: 0;
    width: 1059px;
    height: 1200px;
    overflow: hidden;
    background: var(--page);
  }
  .board {
    position: relative;
    width: 1059px;
    height: 1200px;
  }
  .sign {
    position: absolute;
    left: 148px;
    top: 108px;
    width: 763px;
    height: 423px;
  }
  .sign .display {
    font-family: "Playfair Display", Georgia, serif;
    font-weight: 700;
    font-variant-numeric: lining-nums;
  }
  .sign .tagline {
    font-family: "Playfair Display", Georgia, serif;
    font-weight: 600;
    letter-spacing: 15px;
  }
  .sign .sans {
    font-family: "Josefin Sans", Arial, sans-serif;
    font-weight: 600;
  }
  .site-photo {
    position: absolute;
    top: 641px;
    width: 338px;
    height: 450px;
    background: var(--photo-fill);
  }
  .site-photo--left { left: 151px; }
  .site-photo--right { left: 570px; }
</style>
</head>
<body>
<main class="board">
  <svg class="sign" viewBox="0 0 763 423" role="img" aria-label="Maple Hollow monument sign design">
    <rect class="sign-field" width="763" height="423" fill="var(--sign-sky)"/>
    <polygon class="banner-band" points="0,18 763,0 763,73 0,92" fill="var(--sign-navy)"/>
    <text class="tagline" x="388" y="70" text-anchor="middle" font-size="36" fill="var(--sign-gold)" transform="rotate(-2 388 58)">NEWLY RENOVATED!</text>
    <text class="display" x="381" y="170" text-anchor="middle" font-size="82" fill="var(--sign-white)">Maple Hollow</text>
    <text class="sans" x="381" y="224" text-anchor="middle" font-size="33" letter-spacing="5" fill="var(--sign-white)">APARTMENT COMMUNITY</text>
    <rect class="phone-band" x="0" y="247" width="763" height="110" fill="var(--sign-navy)"/>
    <text class="display" x="381" y="336" text-anchor="middle" font-size="92" fill="var(--sign-gold)">555 - 318 - 7096</text>
    <text class="sans" x="381" y="404" text-anchor="middle" font-size="30" fill="var(--sign-white)">www.maplehollowliving-example.com</text>
  </svg>

  <div class="site-photo site-photo--left" role="img" aria-label="Photo of the sign installed on its pole beside a highway brick wall, seen from below"></div>
  <div class="site-photo site-photo--right" role="img" aria-label="Photo of the installed sign on its pole above a brick wall next to the road"></div>
</main>
</body>
</html>
```